Home Page Graphic/Animation (Marketing)

Brightpath Tutor is a Learning Management System provider. We are in the final stages of building our new website and need help with one key element.

We need to create a graphic with animation that will show up on the front page of our new website. Below are some examples of the style we are aiming for:

https://www.dealvoro.example/
https://www.paperquill.example/
https://www.taskmoro.example/

These are just examples of what we like - We are not asking to create a copy of these - But style elements may be borrowed.

For the graphic/animation, we don’t need actual screenshots of the system shown, but we would like these elements to be artistic/semi-abstract in style, but still be accurate to our software. We would like to limit the use of words in the graphic. Please use the color palette shown in either/both the attached screenshot and/or what you see in the product samples in the video links provided. Here are the sections we’d like to highlight in our system and videos of these sections, which will help you understand what our system looks like:

* Administrator LMS – Adding a course (please include a little pop-up with a certificate of completion or a badge) - https://www.brightpathtutor.example/resources/video-detail/how-to-create-an-online-course1
* Administrator LMS – Assigning or editing a Learner page - https://www.brightpathtutor.example/resources/video-detail/updated-directed-learning-feature
* Administrator LMS – Running a report - https://www.vidstreamly.example/watch?v=qRtKm82bXyP&t=1s
* Learner LMS – Clicking through the Learning Paths page to find and take a course (please include our circle progress bars) - https://www.brightpathtutor.example/resources/video-detail/brightpath-tutor-lms-user-overview

I have attached a screenshot of our new home page with the area where this graphic/animation will be placed.

Ultimately, this graphic/animation will mainly serve as eye candy. We want it to be something that makes our product feel well-designed, and technical and draws folks to want to learn more - All without being overly distracting. Think about how this animation can tell a subconscious story.

Target Market(s)

Corporate Education

Industry/Entity Type

E-Learning / Learning Management System

Number of Pages Required

1 page

Font styles to use
Sans Serif

Requirements
Must have
• Animation / Motion Graphic

```html
<!DOCTYPE html>
<html lang="en">
<head>
<meta charset="utf-8">
<title>Brightpath Tutor – LMS Dashboard Graphic</title>
<link href="https://fonts.googleapis.com/css2?family=Poppins:wght@400;500;600;700&display=swap" rel="stylesheet">
<style>
  :root {
    --bg: #000000;
    --frame-blue: #5cb6d4;
    --screen: #ececec;
    --sidebar: #f8f8f8;
    --sage: #b9c8bb;
    --sage-light: #c6d4c8;
    --sage-dark: #6d7b71;
    --line: #c3cec5;
    --row: #f7f7f7;
    --track: #dcdcdc;
    --orange: #f7950f;
    --yellow: #fbd24a;
    --white: #ffffff;
    --ink: #3b3f3c;
    --green: #8cc152;
    --red: #ee4a24;
  }
  html, body {
    margin: 0;
    padding: 0;
    width: 1200px;
    height: 913px;
    overflow: hidden;
    background: var(--bg);
    font-family: "Poppins", sans-serif;
  }
  .dashboard-graphic { display: block; width: 1200px; height: 913px; }
  .profile-name { font-family: "Poppins", sans-serif; font-size: 11px; font-weight: 500; fill: var(--white); }
  .profile-region { font-family: "Poppins", sans-serif; font-size: 6px; font-weight: 400; fill: var(--white); }
  .card-title { font-family: "Poppins", sans-serif; font-size: 17px; font-weight: 600; fill: var(--white); }
  .donut-value { font-family: "Poppins", sans-serif; font-size: 28px; font-weight: 600; fill: var(--ink); }
  .panel-heading { font-family: "Poppins", sans-serif; font-size: 13px; font-weight: 600; fill: var(--ink); }
  .panel-action { font-family: "Poppins", sans-serif; font-size: 11px; font-weight: 600; fill: var(--ink); }
</style>
</head>
<body>
<svg class="dashboard-graphic" viewBox="0 0 670 510" xmlns="http://www.w3.org/2000/svg">
  <!-- Tablet frame -->
  <g class="tablet">
    <rect x="32" y="78" width="562" height="364" rx="24" fill="var(--frame-blue)"/>
    <rect x="50" y="92" width="530" height="336" rx="6" fill="var(--screen)"/>
    <rect x="50" y="92" width="105" height="336" fill="var(--sidebar)"/>
  </g>

  <!-- Sidebar navigation -->
  <g class="sidebar-nav">
    <rect x="56" y="120" width="22" height="22" rx="4" fill="var(--sage-light)"/>
    <rect x="83" y="124" width="50" height="4" fill="var(--line)"/><rect x="83" y="133" width="56" height="4" fill="var(--line)"/>
    <rect x="56" y="153" width="22" height="22" rx="4" fill="var(--sage-dark)"/>
    <rect x="63" y="158" width="8" height="12" rx="2" fill="var(--white)"/>
    <rect x="83" y="157" width="50" height="5" fill="var(--sage-dark)"/><rect x="83" y="166" width="56" height="5" fill="var(--sage-dark)"/>
    <rect x="56" y="186" width="22" height="22" rx="4" fill="var(--sage-light)"/>
    <rect x="83" y="190" width="50" height="4" fill="var(--line)"/><rect x="83" y="199" width="56" height="4" fill="var(--line)"/>
    <rect x="56" y="218" width="22" height="22" rx="4" fill="var(--sage-light)"/>
    <rect x="83" y="222" width="50" height="4" fill="var(--line)"/><rect x="83" y="231" width="56" height="4" fill="var(--line)"/>
    <rect x="56" y="251" width="22" height="22" rx="4" fill="var(--sage-light)"/>
    <rect x="83" y="255" width="50" height="4" fill="var(--line)"/><rect x="83" y="264" width="56" height="4" fill="var(--line)"/>
    <rect x="56" y="284" width="22" height="22" rx="4" fill="var(--sage-light)"/>
    <rect x="83" y="288" width="50" height="4" fill="var(--line)"/><rect x="83" y="297" width="56" height="4" fill="var(--line)"/>
  </g>

  <!-- Learner profile card -->
  <g class="profile-card">
    <rect x="176" y="122" width="176" height="78" rx="8" fill="var(--sage)"/>
    <rect x="181" y="127" width="66" height="69" rx="6" fill="var(--sage-light)" stroke="var(--white)" stroke-width="1.2" role="img" aria-label="Learner avatar placeholder"/>
    <text class="profile-name" x="255" y="139">Robin</text>
    <text class="profile-name" x="255" y="152">Hale</text>
    <rect x="255" y="162" width="92" height="0.8" fill="var(--white)"/>
    <text class="profile-region" x="255" y="173">Global</text>
    <rect x="361" y="122" width="90" height="78" rx="8" fill="var(--sage)"/>
  </g>

  <!-- Tabs and table -->
  <g class="tabs">
    <rect x="176" y="223" width="53" height="23" rx="2" fill="var(--sage-dark)"/>
    <rect x="238" y="223" width="53" height="23" rx="2" fill="var(--sage-light)"/>
    <rect x="299" y="223" width="53" height="23" rx="2" fill="var(--sage-light)"/>
    <rect x="360" y="223" width="53" height="23" rx="2" fill="var(--sage-light)"/>
    <rect x="421" y="223" width="53" height="23" rx="2" fill="var(--sage-light)"/>
    <rect x="482" y="223" width="53" height="23" rx="2" fill="var(--sage-light)"/>
    <rect x="176" y="255" width="360" height="23" rx="2" fill="var(--sage-dark)"/>
  </g>
  <g class="progress-table">
    <rect x="176" y="290" width="241" height="13" rx="2" fill="var(--row)"/>
    <rect x="423" y="293" width="113" height="6" fill="var(--track)"/><rect x="423" y="293" width="99" height="6" fill="var(--orange)"/>
    <rect x="176" y="310" width="241" height="13" rx="2" fill="var(--row)"/>
    <rect x="423" y="313" width="113" height="6" fill="var(--track)"/><rect x="423" y="313" width="90" height="6" fill="var(--orange)"/>
    <rect x="176" y="331" width="241" height="13" rx="2" fill="var(--row)"/>
    <rect x="423" y="334" width="113" height="6" fill="var(--track)"/><rect x="423" y="334" width="102" height="6" fill="var(--orange)"/>
    <rect x="176" y="352" width="241" height="13" rx="2" fill="var(--row)"/>
    <rect x="423" y="355" width="113" height="6" fill="var(--track)"/><rect x="423" y="355" width="42" height="6" fill="var(--orange)"/>
    <rect x="176" y="373" width="241" height="13" rx="2" fill="var(--row)"/>
    <rect x="423" y="376" width="113" height="6" fill="var(--track)"/><rect x="423" y="376" width="74" height="6" fill="var(--orange)"/>
    <rect x="176" y="393" width="241" height="13" rx="2" fill="var(--row)"/>
    <rect x="423" y="396" width="113" height="6" fill="var(--track)"/><rect x="423" y="396" width="42" height="6" fill="var(--orange)"/>
  </g>

  <!-- Reports card -->
  <g class="reports-card">
    <rect x="440" y="12" width="197" height="195" rx="14" fill="var(--white)"/>
    <path d="M454 12 H623 A14 14 0 0 1 637 26 V47 H440 V26 A14 14 0 0 1 454 12 Z" fill="var(--sage-dark)"/>
    <text class="card-title" x="458" y="37">Reports</text>
    <circle cx="538" cy="113" r="45" fill="none" stroke="var(--orange)" stroke-width="9"/>
    <circle cx="538" cy="113" r="45" fill="none" stroke="var(--yellow)" stroke-width="9"
            stroke-dasharray="28.3 254.4" transform="rotate(-90 538 113)"/>
    <text class="donut-value" x="538" y="123" text-anchor="middle">10%</text>
    <rect x="462" y="177" width="12" height="12" fill="var(--orange)"/>
    <rect x="480" y="178" width="52" height="3" fill="var(--line)"/><rect x="480" y="185" width="52" height="3" fill="var(--line)"/>
    <rect x="547" y="177" width="12" height="12" fill="var(--frame-blue)"/>
    <rect x="565" y="178" width="52" height="3" fill="var(--line)"/><rect x="565" y="185" width="52" height="3" fill="var(--line)"/>
  </g>

  <!-- Search course panel -->
  <g class="search-course-panel">
    <rect x="14" y="320" width="268" height="172" rx="14" fill="var(--white)"/>
    <text class="panel-heading" x="35" y="348">Search Course</text>
    <text class="panel-action" x="192" y="348">Add Course</text>
    <rect x="35" y="363" width="148" height="17" rx="2" fill="var(--orange)"/>
    <rect x="190" y="363" width="81" height="17" rx="2" fill="var(--orange)"/>

    <circle cx="45" cy="403" r="11" fill="var(--sage-light)"/>
    <rect x="63" y="396" width="82" height="4" fill="var(--line)"/><rect x="63" y="405" width="40" height="4" fill="var(--line)"/>
    <rect x="157" y="397" width="24" height="8" rx="4" fill="var(--green)"/><circle cx="177" cy="401" r="3" fill="var(--white)"/>
    <rect x="190" y="399" width="36" height="4" fill="var(--line)"/><rect x="233" y="399" width="36" height="4" fill="var(--line)"/>

    <circle cx="45" cy="432" r="11" fill="var(--sage-light)"/>
    <rect x="63" y="425" width="82" height="4" fill="var(--line)"/><rect x="63" y="434" width="40" height="4" fill="var(--line)"/>
    <rect x="157" y="426" width="24" height="8" rx="4" fill="var(--red)"/><circle cx="161" cy="430" r="3" fill="var(--white)"/>
    <rect x="190" y="428" width="36" height="4" fill="var(--line)"/><rect x="233" y="428" width="36" height="4" fill="var(--line)"/>

    <circle cx="45" cy="461" r="11" fill="var(--sage-light)"/>
    <rect x="63" y="454" width="82" height="4" fill="var(--line)"/><rect x="63" y="463" width="40" height="4" fill="var(--line)"/>
    <rect x="157" y="455" width="24" height="8" rx="4" fill="var(--green)"/><circle cx="177" cy="459" r="3" fill="var(--white)"/>
    <rect x="190" y="457" width="36" height="4" fill="var(--line)"/><rect x="233" y="457" width="36" height="4" fill="var(--line)"/>
  </g>
</svg>
</body>
</html>
```